Flyer für Anbieter von Sportkursen
Zielgruppe
Wir sind ein Anbieter für Sportkurse insbesondere Kickboxen, Fitness, Fightflow und Mobility & Stretch.
Aufgabenstellung
Ich würde gerne die Kickboxkurse (Jugendliche & Erwachsene und Kinder) bewerben. Wenn möglich sollte ich die Enddatei selber anpassen können in Zukunft bei Änderungen. Sportcenter Hubrich ist die Trainingshalle und Taremo Martial Arts der Verein. Das Design sollte sich schwarz/grün (Clubfarben) orientieren.
Seite 1 sollte sich um das Kindertraining handeln und Seite 2 um das Jugendliche & Erwachsenen Training.
Inhalt Kindertraining
Trainingstage: Montag & Donnerstag 18:00 bis 19:00 Uhr / Mittwoch 16:30 bis 17:30 Uhr
Alter: 6 - 13 Jahre
Voranmeldung: www.taremo.li/probetraining / +41 78 294 07 86
Trainingsort: Sportcenter Hubrich, Wiesenhofweg 17, 9488 Talried
Slogan: Taremo Kids | mehr als nur Kickboxen!
Text:
In unserem Kindertraining von 6 - 13 Jahre geht es um mehr als nur Kickboxen. Wir möchten den Kindern Spass am Sport und an der Bewegung vermitteln und dabei wichtige Werte wie Durchsetzungsvermögen, Respekt, Disziplin und Höflichkeit lehren. Die Kinder lernen sich Ziele zu setzen und diese mit Fleiss und Zielstrebigkeit zu erreichen.
Inhalt Jugendliche & Erwachsene
Trainingstage: Montag & Mittwoch 19:15 bis 20:30 Uhr
Alter: ab 14 Jahre
Slogan: Deine beste Stunde des Tages!
Du möchtest fit werden oder deine Fitness steigern? Dann kick dich fit und erlebe deine beste Stunde des Tages. In unserem Kickbox-Gruppentraining legen wir viel Wert auf Rumpfstabilisation, Mobilität, Koordination und natürlich Freude an der Bewegung.
Es werden keine Vorkenntnisse benötigt und alle Fitnesslevel sind bei uns willkommen.

```html
<!DOCTYPE html>
<html lang="de">
<head>
<meta charset="utf-8">
<title>Taremo Kickbox-Flyer</title>
<link rel="stylesheet" href="https://fonts.googleapis.com/css2?family=Anton&family=Rubik:wght@400;500&display=swap">
<style>
  :root{
    --stage:#b3b3b3;
    --black:#0b0b0b;
    --green:#6fb23f;
    --white:#ffffff;
    --muted:#d9d9d9;
    --rule:#8a8a8a;
    --blue:#2a8fd6;
  }
  *{margin:0;padding:0;box-sizing:border-box}
  html,body{width:1200px;height:1117px;overflow:hidden;background:var(--stage)}
  body{position:relative;font-family:'Rubik',sans-serif;color:var(--white)}

  .flyer{position:absolute;top:184px;width:530px;height:750px;background:var(--black);overflow:hidden;box-shadow:4px 8px 14px rgba(0,0,0,.35)}
  .flyer--kids{left:57px}
  .flyer--adults{left:610px}

  .photo{position:absolute;left:0;width:100%}
  .flyer--kids .photo{top:200px;height:410px;background:linear-gradient(120deg,#2b3a2a 0%,#8a8f95 45%,#d7c8c0 70%,#3a3a3a 100%)}
  .flyer--adults .photo{top:205px;height:400px;background:linear-gradient(110deg,#c9a37a 0%,#8a6b55 30%,#1e1e22 50%,#2d5a8c 75%,#c94060 100%)}
  .edge{position:absolute;left:0;width:100%;display:block}

  .kids-head{position:absolute;left:0;top:0;width:100%;height:240px;background:linear-gradient(180deg,#5a9a33 0%,var(--green) 55%,#7dbd48 100%)}
  .kids-title{position:absolute;left:0;width:100%;top:20px;text-align:center;font-family:'Anton',sans-serif;font-size:90px;line-height:1;letter-spacing:.5px;text-shadow:0 2px 6px rgba(0,0,0,.25)}
  .kids-sub{position:absolute;left:0;width:100%;top:121px;text-align:center;font-family:'Anton',sans-serif;font-size:37px;line-height:1}
  .kids-text{position:absolute;left:34px;right:34px;top:168px;text-align:center;font-size:9.6px;line-height:1.3;z-index:3}

  .adult-title{position:absolute;left:35px;top:30px;font-family:'Anton',sans-serif;font-size:48px;line-height:1.12;text-transform:uppercase}
  .adult-title .accent{color:var(--green)}
  .dot-grid{position:absolute;left:170px;top:30px}
  .adult-text{position:absolute;left:304px;width:200px;top:32px;font-size:9.6px;line-height:1.3;color:var(--muted)}
  .adult-text p+p{margin-top:10px}

  .info{position:absolute;left:0;top:0;width:100%;height:100%;z-index:4}
  .label{position:absolute;height:22px;background:var(--green);color:var(--white);font-family:'Anton',sans-serif;font-size:13.5px;line-height:22px;text-align:center;border-radius:2px;letter-spacing:.3px}
  .value{position:absolute;font-size:9px;line-height:1.4;text-align:center;color:var(--white)}
  .label.c1{left:50px;width:158px}
  .label.c2{left:247px;width:126px}
  .value.c1{left:24px;width:210px}
  .value.c2{left:232px;width:156px}
  .r1{top:606px}
  .r2{top:682px}
  .value.r1{top:634px}
  .value.r2{top:710px}
  .value.single{top:717px}
  .hr{position:absolute;left:50px;width:323px;top:668px;border-top:1px dashed var(--rule)}
  .vr{position:absolute;left:232px;top:606px;height:122px;border-left:1px dashed var(--rule)}

  .club-mark{position:absolute;left:393px;top:616px;width:120px;text-align:center;z-index:5}
  .club-mark .dot{display:block;width:64px;height:64px;border-radius:50%;background:var(--green);margin:0 auto 8px}
  .club-mark .name{font-family:'Anton',sans-serif;font-size:15px;line-height:1.1;color:var(--green)}
  .venue-mark{position:absolute;left:378px;top:646px;width:134px;text-align:center;z-index:5;font-family:'Rubik',sans-serif;font-weight:400;font-size:16px;line-height:1.1;color:var(--blue);text-transform:uppercase;letter-spacing:.5px}
</style>
</head>
<body>

<section class="flyer flyer--kids">
  <div class="photo" role="img" aria-label="Foto: Kinder beim Kickbox-Training mit Handschuhen und Kopfschutz"></div>
  <div class="kids-head"></div>
  <svg class="edge" style="top:228px" width="530" height="30" viewBox="0 0 530 30" aria-hidden="true"><path d="M0 0H530V10L512 16 494 9 470 18 448 11 430 20 404 12 380 21 356 13 330 19 306 10 284 18 258 12 236 20 210 11 186 19 160 13 138 21 112 12 90 18 64 10 40 19 18 12 0 18Z" fill="#7dbd48"/></svg>
  <svg class="edge" style="top:540px" width="530" height="70" viewBox="0 0 530 70" aria-hidden="true"><path d="M0 20L26 14 50 22 78 12 104 24 130 16 158 26 186 18 214 30 242 20 270 28 300 18 328 26 356 16 384 24 412 14 440 22 468 12 496 20 530 10V70H0Z" fill="#0b0b0b"/></svg>
  <h1 class="kids-title">TAREMO KIDS</h1>
  <p class="kids-sub">MEHR ALS NUR KICKBOXEN!</p>
  <p class="kids-text">In unserem Kindertraining von 6 - 13 Jahre geht es um mehr als nur Kickboxen. Wir möchten den Kindern Spass am Sport und an der Bewegung vermitteln und dabei wichtige Werte wie Durchsetzungsvermögen, Respekt, Disziplin und Höflichkeit lehren. Die Kinder lernen sich Ziele zu setzen und diese mit Fleiss und Zielstrebigkeit zu erreichen.</p>

  <div class="info">
    <div class="label c1 r1">TRAININGSTAGE:</div>
    <div class="label c2 r1">VORANMELDUNG:</div>
    <div class="value c1 r1">Montag &amp; Donnerstag 18:00 bis 19:00 Uhr /<br>Mittwoch 16:30 bis 17:30 Uhr</div>
    <div class="value c2 r1">www.taremo.li/probetraining /<br>+41 78 294 07 86</div>
    <div class="hr"></div>
    <div class="vr"></div>
    <div class="label c1 r2">TRAININGSORT:</div>
    <div class="label c2 r2">ALTER:</div>
    <div class="value c1 r2">Sportcenter Hubrich, Wiesenhofweg 17,<br>9488 Talried</div>
    <div class="value c2 single">6 - 13 Jahre</div>
  </div>
  <div class="club-mark"><span class="dot"></span><span class="name">TAREMO<br>MARTIAL ARTS</span></div>
</section>

<section class="flyer flyer--adults">
  <div class="photo" role="img" aria-label="Foto: Trainer in Boxhaltung mit blauen Handschuhen in der Trainingshalle"></div>
  <svg class="edge" style="top:198px" width="530" height="30" viewBox="0 0 530 30" aria-hidden="true"><path d="M0 0H530V14L506 20 482 12 456 22 430 14 404 22 378 12 352 20 326 13 300 22 274 14 248 20 222 12 196 22 170 14 144 20 118 12 92 22 66 14 40 20 14 12 0 16Z" fill="#0b0b0b"/></svg>
  <svg class="edge" style="top:550px" width="530" height="60" viewBox="0 0 530 60" aria-hidden="true"><path d="M0 18L24 10 50 20 76 12 102 22 130 14 156 24 184 16 212 26 240 18 268 26 296 16 324 24 352 14 380 22 408 12 436 20 464 10 492 18 530 8V60H0Z" fill="#0b0b0b"/></svg>
  <h2 class="adult-title">Deine<br><span class="accent">Beste Stunde</span><br>des Tages!</h2>
  <svg class="dot-grid" width="76" height="18" viewBox="0 0 76 18" aria-hidden="true" fill="#ffffff">
    <circle cx="2" cy="2" r="1.3"/><circle cx="14" cy="2" r="1.3"/><circle cx="26" cy="2" r="1.3"/><circle cx="38" cy="2" r="1.3"/><circle cx="50" cy="2" r="1.3"/><circle cx="62" cy="2" r="1.3"/><circle cx="74" cy="2" r="1.3"/>
    <circle cx="2" cy="16" r="1.3"/><circle cx="14" cy="16" r="1.3"/><circle cx="26" cy="16" r="1.3"/><circle cx="38" cy="16" r="1.3"/><circle cx="50" cy="16" r="1.3"/><circle cx="62" cy="16" r="1.3"/><circle cx="74" cy="16" r="1.3"/>
  </svg>
  <div class="adult-text">
    <p>Du möchtest fit werden oder deine Fitness steigern? Dann kick dich fit und erlebe deine beste Stunde des Tages. In unserem Kickbox-Gruppentraining legen wir viel Wert auf Rumpfstabilisation, Mobilität, Koordination und natürlich Freude an der Bewegung.</p>
    <p>Es werden keine Vorkenntnisse benötigt und alle Fitnesslevel sind bei uns willkommen.</p>
  </div>

  <div class="info">
    <div class="label c1 r1">TRAININGSTAGE:</div>
    <div class="label c2 r1">VORANMELDUNG:</div>
    <div class="value c1 r1">Montag &amp; Mittwoch 19:15 bis 20:30 Uhr</div>
    <div class="value c2 r1">www.taremo.li/probetraining /<br>+41 78 294 07 86</div>
    <div class="hr"></div>
    <div class="vr"></div>
    <div class="label c1 r2">TRAININGSORT:</div>
    <div class="label c2 r2">ALTER:</div>
    <div class="value c1 r2">Sportcenter Hubrich, Wiesenhofweg 17,<br>9488 Talried</div>
    <div class="value c2 single">ab 14 Jahre</div>
  </div>
  <div class="venue-mark">Sportcenter<br>Hubrich</div>
</section>

</body>
</html>
```